Corvane Industries business cards

We need business cards for our company Corvane Industries, based in Brisbane but trading world wide. We buy and sell Corvane Industries, generators and marine equipment. The design needs to be kept clean, simple but eye catching.
Please keep with our current logo (included) and further information can be included on request

Business

0792cd
33a6d7
85cae6
3276b5
0455a3
cedeed
cee9f5
ffffff

```html
<!DOCTYPE html>
<html lang="en">
<head>
<meta charset="utf-8">
<title>Corvane Industries – Business Card</title>
<link rel="stylesheet" href="https://fonts.googleapis.com/css2?family=Open+Sans:wght@400;600&family=Arimo:wght@700&display=swap">
<style>
  :root {
    --page-bg: #e9edf2;
    --card-deep: #0455a3;
    --card-mid: #3276b5;
    --card-bright: #0792cd;
    --ink-white: #ffffff;
    --ink-soft: #cedeed;
    --ink-pale: #cee9f5;
  }
  * { margin: 0; padding: 0; box-sizing: border-box; }
  html, body {
    width: 1200px; height: 803px; overflow: hidden;
    background: var(--page-bg);
  }
  .stage {
    width: 1200px; height: 803px;
    display: flex; align-items: center; justify-content: center;
  }
  .business-card {
    position: relative;
    width: 900px; height: 514px;
    background: linear-gradient(160deg, var(--card-mid) 0%, var(--card-deep) 100%);
    box-shadow: 0 14px 40px rgba(4, 40, 80, 0.25);
    color: var(--ink-white);
    overflow: hidden;
  }
  .brand {
    position: absolute; left: 40px; top: 62px;
    display: flex; align-items: center; gap: 22px;
  }
  .brand-mark {
    width: 92px; height: 92px;
    background: var(--ink-white);
    border-radius: 10px;
  }
  .brand-name {
    font-family: "Open Sans", sans-serif;
    font-weight: 400;
    font-size: 50px; line-height: 50px;
    color: var(--ink-white);
  }
  .brand-suffix {
    display: block;
    font-family: "Open Sans", sans-serif;
    font-size: 14px; line-height: 18px;
    color: var(--ink-white);
    text-align: right;
    margin-top: 2px;
  }
  .holder-name {
    position: absolute; right: 40px; top: 62px;
    font-family: "Open Sans", sans-serif;
    font-size: 30px; font-weight: 400;
    letter-spacing: 0.5px;
  }
  .contact-lines {
    position: absolute; right: 40px; top: 188px;
    list-style: none;
    font-family: "Arimo", sans-serif; font-weight: 700;
    font-size: 22px; line-height: 32px;
  }
  .contact-lines li {
    display: flex; align-items: center; justify-content: flex-end; gap: 8px;
  }
  .contact-lines svg { fill: var(--ink-white); }
  .postal {
    position: absolute; left: 160px; top: 356px;
    font-family: "Arimo", sans-serif; font-weight: 700;
    font-size: 28px; line-height: 34px;
    color: var(--ink-soft);
    text-align: center;
  }
  .web {
    position: absolute; right: 40px; top: 432px;
    font-family: "Arimo", sans-serif; font-weight: 700;
    font-size: 22px; color: var(--ink-pale);
  }
  .email {
    position: absolute; left: 24px; bottom: 18px;
    font-family: "Arimo", sans-serif; font-weight: 700;
    font-size: 22px; color: var(--ink-pale);
  }
</style>
</head>
<body>
<main class="stage">
  <article class="business-card">
    <div class="brand">
      <div class="brand-mark"></div>
      <div class="brand-name">Corvane<br>Industries<span class="brand-suffix">Pty Ltd</span></div>
    </div>

    <p class="holder-name">Marla Tessin</p>

    <ul class="contact-lines">
      <li>
        <svg width="14" height="18" viewBox="0 0 14 18" aria-label="Phone"><path d="M3 1c1 0 2 3 2 4s-2 1-2 2 2 5 3 5 1-2 2-2 4 1 4 2-1 4-3 4C5 16 0 10 0 5 0 3 2 1 3 1z"/></svg>
        61 7 3000 4821
      </li>
      <li>
        <svg width="12" height="20" viewBox="0 0 12 20" aria-label="Mobile"><path d="M2 0h8a2 2 0 0 1 2 2v16a2 2 0 0 1-2 2H2a2 2 0 0 1-2-2V2a2 2 0 0 1 2-2zm0 3v12h8V3z"/></svg>
        61 400 572 918
      </li>
      <li>
        <svg width="28" height="18" viewBox="0 0 28 18" aria-label="Fax"><rect x="0" y="5" width="28" height="13" rx="2"/><rect x="6" y="0" width="16" height="6"/></svg>
        61 7 3000 4830
      </li>
    </ul>

    <p class="postal">18 Harbourline Road, Eastvale QLD 4172<br>PO Box 560, Riverton QLD 4170</p>

    <p class="web">www.corvane-industries.com.au</p>
    <p class="email">marla@corvane-industries.com.au</p>
  </article>
</main>
</body>
</html>
```